Poetry Book Cover Design Project

Looking for a minimalistic book cover design for a collection of poems. The book title is "Before The Morning Turns To Glass". There are three parts to the book. First covers poetry in the theme of Rage. Second love and desire. The third is strange poems. Essentially the sections are "Rage", "Desire" and the "Strange". The reason for the title "Before The Morning Turns To Glass" is as if someone is writing these till life changes towards the intended outcome as felt in each poem. I want to have the author's name "Nirosha Kulathunge" at the bottom. Ilustration attached.
- Minimalistic

```html
<!DOCTYPE html>
<html lang="en">
<head>
<meta charset="UTF-8">
<title>Before The Morning Turns To Glass — Nirosha Kulathunge</title>
<link rel="stylesheet" href="https://fonts.googleapis.com/css2?family=Crimson+Pro:wght@600;700&display=swap">
<style>
  :root {
    --paper: #efefef;
    --paper-shade: #e2e2e2;
    --title-blue: #0557a6;
    --band-teal: #5bc6d8;
    --author-ink: #0d0d0d;
    --pencil-wood: #e6b48a;
    --pencil-wood-dark: #d39c6c;
  }
  html, body {
    margin: 0;
    padding: 0;
    width: 800px;
    height: 1200px;
    overflow: hidden;
    background: var(--paper);
  }
  .cover {
    position: relative;
    width: 800px;
    height: 1200px;
    overflow: hidden;
    background: linear-gradient(135deg, #f5f5f5 0%, var(--paper) 55%, var(--paper-shade) 100%);
  }
  .cover-art {
    position: absolute;
    inset: 0;
  }
  .title {
    position: absolute;
    right: 54px;
    top: 50px;
    margin: 0;
    text-align: right;
    font-family: "Crimson Pro", "Minion Pro", Georgia, serif;
    font-weight: 700;
    font-size: 106px;
    line-height: 124px;
    letter-spacing: -1px;
    color: var(--title-blue);
  }
  .title span { display: block; }
  .author {
    position: absolute;
    right: 54px;
    bottom: 60px;
    margin: 0;
    font-family: "Crimson Pro", "Minion Pro", Georgia, serif;
    font-weight: 700;
    font-size: 34px;
    letter-spacing: 1px;
    color: var(--author-ink);
  }
</style>
</head>
<body>
  <main class="cover">
    <svg class="cover-art" width="800" height="1200" viewBox="0 0 800 1200">
      <defs>
        <linearGradient id="pencil-tone" x1="0" x2="1" y1="0" y2="0">
          <stop offset="0" stop-color="var(--pencil-wood)"/>
          <stop offset="1" stop-color="var(--pencil-wood-dark)"/>
        </linearGradient>
      </defs>
      <polygon class="chevron-band" fill="var(--band-teal)"
               points="800,173 800,263 132,928 404,1200 315,1200 43,928"/>
      <rect class="pencil-photo" role="img" aria-label="Photograph of a sharpened wooden pencil pointing upward"
            x="228" y="575" width="80" height="625" fill="url(#pencil-tone)"/>
    </svg>

    <h1 class="title">
      <span>Before</span>
      <span>The</span>
      <span>Morning</span>
      <span>Turns</span>
      <span>To</span>
      <span>Glass</span>
    </h1>

    <p class="author">Nirosha Kulathunge</p>
  </main>
</body>
</html>
```